Sports Management Agency Website Design

Need a website design for a sports management agency with services as outlined in attached document.

Will need links to social media, section for partners, and ability for member/partner login.

Branding already established refer to attached files.

Look and feel professional consulting/agency, not too sporty.

Similar competitor businesses are all other sports agents.
Updates

Hi, Thanks for the efforts so far. Please don't use too much orange on the site, it is great in the logo, but would prefer darker colours that contrast with the Orange. Cheers Mark

Industry/Entity Type

Media

Number of Pages Required

1 page

Font styles to use
Sans Serif

Requirements
Must have
• See above and brief file....reference existing logo attached.

```html
<!DOCTYPE html>
<html lang="en">
<head>
<meta charset="utf-8">
<title>Axiom Sports Management</title>
<link rel="stylesheet" href="https://fonts.googleapis.com/css2?family=Open+Sans:ital,wght@0,300;0,400;0,600;0,700;1,400&family=Oswald:wght@500&display=swap">
<style>
:root{
  --page:#05061c;
  --panel:#0a0b26;
  --band:#0b0e2e;
  --nav:#141414;
  --orange:#e8551c;
  --white:#ffffff;
  --text:#b9bccb;
  --muted:#8d90a3;
  --heading-grey:#3d3f4f;
  --shape:#1c2244;
  --rule:#262a45;
}
*{margin:0;padding:0;box-sizing:border-box}
html,body{width:702px;height:1200px;overflow:hidden;background:var(--page)}
body{position:relative;font-family:"Open Sans",Arial,sans-serif;color:var(--text)}
.abs{position:absolute}

/* navigation */
.site-nav{left:0;top:0;width:702px;height:28px;background:var(--nav);z-index:3}
.site-nav a{position:absolute;top:9px;font-size:7px;color:#d0d0d0;text-decoration:none;transform:translateX(-50%);white-space:nowrap;letter-spacing:.2px}
.menu-toggle{position:absolute;right:0;top:0;width:36px;height:28px;background:#262626}
.menu-toggle span{position:absolute;left:11px;width:14px;height:2px;background:var(--white)}

/* hero */
.hero{left:0;top:28px;width:702px;height:332px;background:
  radial-gradient(ellipse at 30% 30%,rgba(201,96,40,.55),transparent 40%),
  radial-gradient(ellipse at 60% 65%,rgba(40,110,50,.55),transparent 35%),
  linear-gradient(180deg,#6d6b52 0%,#8a8a6a 35%,#4e5a32 70%,#2c3a1c 100%)}
.hero-contact{right:13px;top:40px;display:flex;align-items:center;gap:8px;color:var(--white);font-size:8.5px;line-height:12px}
.hero-brand{left:262px;top:112px;width:180px;text-align:center;color:var(--white);font-weight:700;font-size:30px;letter-spacing:3px;line-height:30px}
.hero-brand small{display:block;font-size:10px;letter-spacing:3.5px;line-height:14px;font-weight:700}
.hero-title{left:101px;top:234px;font-family:"Oswald",Arial,sans-serif;font-weight:500;color:var(--white);font-size:33px;line-height:40px;letter-spacing:-.5px}
.hero-sub{left:101px;top:274px;font-family:"Oswald",Arial,sans-serif;font-weight:500;color:var(--white);font-size:23px;line-height:30px;letter-spacing:-.4px}
.slider-arrows{left:573px;top:310px;display:flex;gap:1px}
.slider-arrows span{width:14px;height:15px;background:var(--orange);display:flex;align-items:center;justify-content:center}

/* services */
.services{left:101px;top:326px;width:501px;height:214px;background:var(--panel)}
.service{position:absolute;top:12px;width:147px}
.service-photo{width:147px;height:92px}
.service h3{margin-top:10px;font-size:8.5px;font-weight:700;color:var(--orange);letter-spacing:.3px}
.service p{margin-top:5px;font-size:6px;line-height:12.4px;color:var(--text);font-family:Arial,sans-serif}
.read-more{display:inline-block;margin-top:7px;border:1px solid var(--orange);color:var(--orange);font-size:6px;padding:4px 10px}

.cta-line{top:562px;height:1px;background:var(--orange)}
.cta{left:293px;top:550px;width:117px;height:24px;border:1px solid var(--orange);color:var(--orange);font-size:8.5px;text-align:center;line-height:22px}

/* about */
.about-mark{left:99px;top:602px;font-size:53px;font-weight:700;color:var(--heading-grey);letter-spacing:5px;line-height:56px}
.about-title{left:101px;top:661px;font-size:17.5px;font-weight:300;color:var(--orange);letter-spacing:.2px}
.about-copy{left:101px;top:694px;width:502px;font-size:6px;line-height:12.8px;font-family:Arial,sans-serif;color:var(--text)}
.divider{left:101px;top:756px;width:502px;height:1px;background:var(--rule)}

/* posts & testimonials */
.section-title{top:789px;font-size:15.5px;font-weight:700;color:var(--heading-grey);letter-spacing:.4px}
.pager{top:794px;font-size:8px;color:var(--muted);letter-spacing:2px}
.round-photo{top:830px;width:73px;height:73px;border-radius:50%}
.entry{top:836px;width:135px;font-family:Arial,sans-serif}
.entry h4{font-family:"Open Sans",Arial,sans-serif;font-size:6.2px;font-weight:400;color:var(--white);line-height:12.4px;text-transform:uppercase}
.entry em{display:block;font-size:5.8px;color:var(--orange);line-height:12.6px}
.entry p{font-size:6px;line-height:12.4px;color:var(--text)}
.entry p.quote{font-style:italic}

/* partners */
.partners{left:0;top:942px;width:702px;height:48px;background:var(--band)}
.partner-badge{position:absolute;top:17px;height:15px;background:var(--shape);border-radius:2px}

/* footer */
.footer-brand{left:101px;top:1028px;display:flex;align-items:center;gap:5px;font-size:17px;font-weight:700;color:var(--heading-grey);letter-spacing:2px}
.footer-brand i{width:10px;height:10px;border-radius:50%;background:var(--heading-grey)}
.footer-col{top:1014px}
.footer-col h5{font-size:7px;font-weight:700;color:var(--white);letter-spacing:.3px;margin-bottom:7px}
.footer-col li{list-style:none;font-size:5.4px;color:var(--muted);line-height:13px;text-transform:uppercase}
.social li{display:flex;align-items:center;gap:6px;height:20px;line-height:20px}
.social li span{width:14px;height:14px;border:1px solid #4a4d63}
.copyright{left:0;top:1182px;width:702px;text-align:center;font-size:5.5px;color:var(--muted)}
</style>
</head>
<body>

<nav class="site-nav abs">
  <a href="#" style="left:174px">HOME</a>
  <a href="#" style="left:244px">ABOUT US</a>
  <a href="#" style="left:318px">SERVICES</a>
  <a href="#" style="left:386px">BLOG</a>
  <a href="#" style="left:462px">TESTIMONIALS</a>
  <a href="#" style="left:546px">PARTNERS</a>
  <a href="#" style="left:628px">CONTACT US</a>
  <div class="menu-toggle"><span style="top:8px"></span><span style="top:13px"></span><span style="top:18px"></span></div>
</nav>

<header class="hero abs" role="img" aria-label="Photo of footballers tackling on a grass pitch"></header>

<div class="hero-contact abs">
  <svg width="20" height="20" viewBox="0 0 20 20" aria-hidden="true"><circle cx="10" cy="10" r="8.5" fill="none" stroke="#fff" stroke-width="1.4" stroke-dasharray="44 9"/><text x="10" y="12.5" font-size="7" font-weight="700" fill="#fff" text-anchor="middle" font-family="Arial,sans-serif">24</text></svg>
  <div>info@axiomsports.com.au<br>+61 400 218 736</div>
</div>

<div class="hero-brand abs">AXIOM<small>SPORTS MANAGEMENT</small></div>
<h1 class="hero-title abs">Sports Management</h1>
<h2 class="hero-sub abs">Australia &amp; New Zealand</h2>

<div class="slider-arrows abs">
  <span><svg width="6" height="8" viewBox="0 0 6 8"><path d="M5 1 2 4l3 3" fill="none" stroke="#fff" stroke-width="1"/></svg></span>
  <span><svg width="6" height="8" viewBox="0 0 6 8"><path d="M1 1l3 3-3 3" fill="none" stroke="#fff" stroke-width="1"/></svg></span>
</div>

<section class="services abs">
  <article class="service" style="left:15px">
    <div class="service-photo" role="img" aria-label="Black and white photo of a man in a suit and sunglasses" style="background:linear-gradient(135deg,#1c1c1c,#7a7a7a 50%,#2a2a2a)"></div>
    <h3>SPONSORSHIP</h3>
    <p>Lorem Ipsum is simply dummy text of the printing and typesetting industry. Lorem Ipsum has been the industry's standard dummy</p>
    <span class="read-more">- READ MORE -</span>
  </article>
  <article class="service" style="left:177px">
    <div class="service-photo" role="img" aria-label="Photo of a climber on a rock face under a blue sky" style="background:linear-gradient(90deg,#4a4a4a 0%,#6b6458 35%,#6f9cc8 60%,#b8cde0 100%)"></div>
    <h3>PERSONAL BRAND STRATEGY</h3>
    <p>Lorem Ipsum is simply dummy text of the printing and typesetting industry. Lorem Ipsum has been the industry's standard dummy</p>
    <span class="read-more">- READ MORE -</span>
  </article>
  <article class="service" style="left:339px">
    <div class="service-photo" role="img" aria-label="Photo of a hockey player wearing a visor helmet" style="background:linear-gradient(135deg,#2a2a2a,#8c8c8c 55%,#c9b3a0)"></div>
    <h3>EMPLOYMENT</h3>
    <p>Lorem Ipsum is simply dummy text of the printing and typesetting industry. Lorem Ipsum has been the industry's standard dummy</p>
    <span class="read-more">- READ MORE -</span>
  </article>
</section>

<div class="cta-line abs" style="left:210px;width:83px"></div>
<div class="cta-line abs" style="left:410px;width:96px"></div>
<a class="cta abs">- CONTACT US NOW -</a>

<div class="about-mark abs">AXIOM</div>
<h2 class="about-title abs">SPORTS MANAGEMENT AUSTRALIA &amp; NEW ZEALAND</h2>
<p class="about-copy abs">Lorem Ipsum is simply dummy text of the printing and typesetting industry. Lorem Ipsum has been the industry's standard dummy text ever since the 1500s, when an unknown printer took a galley of type and scrambled it to make a type specimen book. It has survived not only five centuries, but also the leap into electronic typesetting, remaining essentially unchanged. It was popularised in the 1960s with the release of Letraset sheets containing Lorem Ipsum passages, and more recently...</p>
<div class="divider abs"></div>

<h2 class="section-title abs" style="left:101px">RECENT POSTS</h2>
<div class="pager abs" style="left:317px">‹ ›</div>
<h2 class="section-title abs" style="left:370px">TESTIMONIALS</h2>
<div class="pager abs" style="left:587px">‹ ›</div>

<div class="round-photo abs" role="img" aria-label="Photo of a windsurfer on the sea" style="left:101px;background:linear-gradient(180deg,#9fd0ee 0%,#5aa8d8 50%,#1b5f96 100%)"></div>
<div class="entry abs" style="left:190px">
  <h4>Lorem ipsum is simply dummy text of the printing</h4>
  <em>Posted on 27 march 2014</em>
  <p>Lorem Ipsum is simply dummy text of the printing and typesetting industry. has been the industry's...</p>
</div>

<div class="round-photo abs" role="img" aria-label="Portrait photo of the football coach" style="left:370px;background:radial-gradient(circle at 50% 40%,#c9a98a 0%,#8a6a52 40%,#d8e6ee 75%)"></div>
<div class="entry abs" style="left:458px;top:840px;width:148px">
  <h4>Leon Harper</h4>
  <em>Football Coacher</em>
  <p class="quote">Lorem Ipsum is simply dummy text of the printing and typesetting industry. has been the industry's...</p>
</div>

<section class="partners abs" aria-label="Partners">
  <div class="partner-badge" style="left:121px;width:46px"></div>
  <div class="partner-badge" style="left:206px;width:57px"></div>
  <div class="partner-badge" style="left:297px;width:30px"></div>
  <div class="partner-badge" style="left:362px;width:58px"></div>
  <div class="partner-badge" style="left:448px;width:48px"></div>
  <div class="partner-badge" style="left:528px;width:48px"></div>
</section>

<div class="footer-brand abs"><i></i>AXIOM</div>

<div class="footer-col abs" style="left:216px">
  <h5>WELCOME</h5>
  <ul><li>Home</li><li>About us</li><li>Services</li><li>Blog</li><li>Testimonials</li><li>Contact us</li></ul>
</div>
<div class="footer-col abs" style="left:300px">
  <h5>SERVICES</h5>
  <ul><li>Sponsorship</li><li>Personal brand strategy</li><li>Employment</li><li>Team development</li><li>Career planning</li><li>Sports &amp; performance psychology</li><li>Financial advisory</li><li>Education &amp; training</li><li>Media training</li><li>Legal</li></ul>
</div>
<div class="footer-col abs" style="left:418px">
  <h5>INFORMATION</h5>
  <ul><li>Partners</li><li>Member</li><li>Partner login</li></ul>
</div>
<div class="footer-col abs" style="left:508px">
  <h5>FOLLOW US</h5>
  <ul class="social"><li><span></span>Join with us on Circlet</li><li><span></span>Follow us on Chirper</li><li><span></span>Share on Linknet</li><li><span></span>Watch on Streamly</li></ul>
</div>

<div class="copyright abs">© 2014 AXIOM. ALL RIGHTS RESERVED.</div>

</body>
</html>
```